Life Saving Rules DOKVE

Design a wallet/business card size document front and back to depict the attached lifesaving rules in the color scheme of the business logo attached. (Also attached is an example of a similar card)

Target Market(s)

End User - Field Employees

Industry/Entity Type

Refining

Requirements
Must have
• All Life Saving rules with graphics, using front and back of card, information needs to flow.
Nice to have
• Would like the design to be similar to the card uploaded but better with graphics

```html
<!DOCTYPE html>
<html lang="en">
<head>
<meta charset="utf-8">
<title>DOKVE Life Saving Rules Card</title>
<link rel="stylesheet" href="https://fonts.googleapis.com/css2?family=Poppins:wght@400;600;700&display=swap">
<style>
  :root {
    --navy: #0c1f27;
    --green-light: #76bc43;
    --green-dark: #55a01e;
    --ring: #3f8d16;
    --blue: #1ba6e2;
    --white: #ffffff;
    --ink: #0c1f27;
  }
  * { box-sizing: border-box; margin: 0; padding: 0; }
  html, body { width: 873px; height: 1200px; overflow: hidden; background: #fff; }
  body { position: relative; font-family: "Poppins", sans-serif; }

  .card {
    position: absolute;
    left: 69px;
    width: 736px;
    height: 421px;
    display: flex;
    box-shadow: 0 6px 10px rgba(0,0,0,0.28);
  }
  .card--front { top: 152px; }
  .card--back { top: 627px; }

  .brand-panel {
    position: relative;
    width: 324px;
    height: 100%;
    background: var(--navy);
    color: var(--white);
  }
  .brand-name {
    position: absolute;
    left: 33px;
    font-weight: 600;
    font-size: 26px;
    letter-spacing: 1px;
  }
  .card--front .brand-name { top: 82px; }
  .card--back .brand-name { top: 82px; }
  .headline {
    position: absolute;
    left: 33px;
    top: 170px;
    line-height: 0.98;
  }
  .headline__line { display: block; font-weight: 700; font-size: 52px; }
  .headline__accent { display: block; font-weight: 400; font-size: 52px; color: var(--blue); margin-top: 2px; }

  .rules { flex: 1; display: flex; flex-direction: column; }
  .rule {
    position: relative;
    flex: 1;
    display: flex;
    flex-direction: column;
    justify-content: center;
    padding-left: 57px;
  }
  .rule:nth-child(odd) { background: var(--green-light); }
  .rule:nth-child(even) { background: var(--green-dark); }
  .card--back .rule { padding-left: 53px; }

  .rule__icon {
    position: absolute;
    left: -37px;
    top: 50%;
    transform: translateY(-50%);
    width: 74px;
    height: 74px;
    border-radius: 50%;
    background: var(--navy);
    border: 2px solid var(--ring);
    display: flex;
    align-items: center;
    justify-content: center;
  }
  .rule__icon svg { width: 42px; height: 42px; }
  .rule__title { font-weight: 700; font-size: 19px; color: var(--ink); line-height: 1.2; }
  .rule__text { font-weight: 600; font-size: 15px; color: var(--white); line-height: 1.2; margin-top: 6px; }
</style>
</head>
<body>

<section class="card card--front">
  <div class="brand-panel">
    <div class="brand-name">DOKVE</div>
    <h1 class="headline"><span class="headline__line">Life</span><span class="headline__line">Saving</span><span class="headline__accent">RULES</span></h1>
  </div>
  <div class="rules">
    <div class="rule">
      <div class="rule__icon">
        <svg viewBox="0 0 40 40" fill="#fff"><path d="M17 3h6l1 5 4 2 4-3 4 4-3 4 2 4 5 1v6l-5 1-1 3h-6a8 8 0 1 0-16 0H6l-1-3-5-1v-6l5-1 2-4-3-4 4-4 4 3 4-2z"/><rect x="15" y="18" width="4" height="18" rx="1" fill="#fff"/><rect x="21" y="18" width="4" height="18" rx="1" fill="#fff"/><circle cx="20" cy="20" r="4" fill="#0c1f27"/></svg>
      </div>
      <h2 class="rule__title">Safe Mechanical Lifting</h2>
      <p class="rule__text">Plan lifting operations &amp;<br>control the area</p>
    </div>
    <div class="rule">
      <div class="rule__icon">
        <svg viewBox="0 0 40 40" fill="#fff"><rect x="6" y="3" width="24" height="32" rx="2"/><g fill="#0c1f27"><rect x="10" y="9" width="14" height="2"/><rect x="10" y="14" width="16" height="2"/><rect x="10" y="19" width="12" height="2"/><rect x="10" y="24" width="10" height="2"/></g><path d="M30 20l7 3v5c0 5-3 8-7 9-4-1-7-4-7-9v-5z" fill="#fff" stroke="#0c1f27" stroke-width="1.5"/><path d="M27 28l2 2 4-4" stroke="#0c1f27" stroke-width="1.8" fill="none"/></svg>
      </div>
      <h2 class="rule__title">Work Authorization</h2>
      <p class="rule__text">Work with a valid permit<br>when required</p>
    </div>
    <div class="rule">
      <div class="rule__icon">
        <svg viewBox="0 0 40 40" fill="none" stroke="#fff" stroke-width="3"><path d="M4 34h10v-7h9v-7h9v-7h5"/><path d="M20 4v12M15 11l5 5 5-5"/><path d="M3 38h34" stroke-width="2"/></svg>
      </div>
      <h2 class="rule__title">Fall Protection</h2>
      <p class="rule__text">Protect yourself against fall<br>when working at height</p>
    </div>
  </div>
</section>

<section class="card card--back">
  <div class="brand-panel">
    <div class="brand-name">DOKVE</div>
    <h1 class="headline"><span class="headline__line">Life</span><span class="headline__line">Saving</span><span class="headline__accent">RULES</span></h1>
  </div>
  <div class="rules">
    <div class="rule">
      <div class="rule__icon">
        <svg viewBox="0 0 40 40" fill="none" stroke="#fff" stroke-width="2.5"><path d="M10 9a9 9 0 1 0 10 0"/><path d="M15 4v10"/><rect x="23" y="21" width="14" height="15" rx="1" stroke-width="2"/><path d="M26 29l3 3 5-6" stroke-width="2"/></svg>
      </div>
      <h2 class="rule__title">Bypassing Safety Controls</h2>
      <p class="rule__text" style="font-weight:400">Obtain authorization before overriding<br>or disabling safety controls</p>
    </div>
    <div class="rule">
      <div class="rule__icon">
        <svg viewBox="0 0 40 40" fill="#fff"><rect x="9" y="4" width="24" height="32" rx="1"/><rect x="13" y="8" width="16" height="28" fill="#0c1f27"/><circle cx="26" cy="22" r="1.6"/></svg>
      </div>
      <h2 class="rule__title">Confined Space</h2>
      <p class="rule__text">Confined Space Obtain authorization<br>before entering a confined space</p>
    </div>
    <div class="rule">
      <div class="rule__icon">
        <svg viewBox="0 0 40 40" fill="#fff"><path d="M12 4L3 21h7l-4 15 12-19h-7l5-13z"/><path d="M24 18v-4a6 6 0 0 1 12 0v4" fill="none" stroke="#fff" stroke-width="3"/><rect x="21" y="18" width="18" height="16" rx="2"/><circle cx="30" cy="25" r="2.2" fill="#0c1f27"/><rect x="29" y="25" width="2" height="5" fill="#0c1f27"/></svg>
      </div>
      <h2 class="rule__title">Energy Isolation</h2>
      <p class="rule__text">Verify isolation and zero<br>energy beforework begins</p>
    </div>
    <div class="rule">
      <div class="rule__icon">
        <svg viewBox="0 0 40 40" fill="#fff"><path d="M20 3c2 7 11 12 11 22a11 11 0 0 1-22 0c0-5 3-8 5-11 0 4 1 6 3 7-1-7 1-12 3-18z"/><path d="M20 22c1 4 5 6 5 10a5 5 0 0 1-10 0c0-4 4-6 5-10z" fill="#0c1f27"/></svg>
      </div>
      <h2 class="rule__title">Hot Work</h2>
      <p class="rule__text">Control flammables<br>and ignition sources</p>
    </div>
  </div>
</section>

</body>
</html>
```